Pelton Mortgage Capital Business Card

We need a business card design for our mortgage servicing company. In addition to servicing the loans of homeowners, we help homeowners with purchasing their homes and any mortgage refinancing. We would like to see designs that use the colors in the logo attached below (gold-ish yellow and navy blue), and any other design you deem fit! The design should communicate a simpler life with smart mortgages provided by Pelton.

```html
<!DOCTYPE html>
<html lang="en">
<head>
<meta charset="UTF-8">
<title>Pelton Mortgage Capital – Business Card</title>
<link rel="stylesheet" href="https://fonts.googleapis.com/css2?family=Arimo:wght@400;700&display=swap">
<style>
  :root {
    --navy: #251f52;
    --gold: #d6b043;
    --gold-deep: #cfa83a;
    --white: #ffffff;
    --paper-edge: #f2f2f2;
    --backdrop: #2b2b2b;
    --text-font: "Arimo", Arial, sans-serif;
  }
  * { box-sizing: border-box; margin: 0; padding: 0; }
  html, body { width: 1200px; height: 750px; overflow: hidden; }
  body {
    background: var(--backdrop);
    font-family: var(--text-font);
    display: flex;
    align-items: center;
    justify-content: center;
    gap: 40px;
  }
  .card {
    position: relative;
    width: 520px;
    height: 300px;
    border-radius: 18px;
    overflow: hidden;
    box-shadow: 0 14px 30px rgba(0,0,0,.45);
  }
  .card--front {
    background: var(--navy);
    display: flex;
    align-items: center;
    justify-content: center;
  }
  .wordmark {
    display: flex;
    align-items: center;
    gap: 12px;
    font-weight: 700;
    color: var(--gold);
  }
  .wordmark__dot {
    border-radius: 50%;
    background: var(--gold);
  }
  .card--front .wordmark { font-size: 44px; }
  .card--front .wordmark__dot { width: 26px; height: 26px; }

  .card--back {
    background: linear-gradient(100deg, var(--gold-deep), var(--gold));
    color: var(--white);
  }
  .card--back .wordmark {
    position: absolute;
    top: 46px;
    right: 60px;
    font-size: 24px;
    color: var(--navy);
    gap: 8px;
  }
  .card--back .wordmark__dot { width: 14px; height: 14px; background: var(--navy); }

  .divider {
    position: absolute;
    left: 38px;
    right: 30px;
    top: 176px;
    height: 1px;
    background: var(--white);
  }
  .person {
    position: absolute;
    left: 40px;
    bottom: 128px;
  }
  .person__name {
    font-size: 20px;
    font-weight: 700;
    color: var(--navy);
    line-height: 1.1;
  }
  .person__title {
    font-size: 14px;
    color: var(--white);
    margin-left: 12px;
  }
  .address {
    position: absolute;
    left: 56px;
    top: 196px;
    font-size: 13px;
    line-height: 1.45;
  }
  .contact {
    position: absolute;
    right: 30px;
    top: 186px;
    list-style: none;
    font-size: 13px;
    line-height: 1.45;
    text-align: right;
  }
  .contact li { display: flex; align-items: center; justify-content: flex-end; gap: 8px; }
  .contact svg { width: 10px; height: 10px; fill: var(--navy); }

  .edge-band {
    position: absolute;
    left: 0; right: 0; bottom: 0;
    height: 16px;
    display: flex;
  }
  .edge-band__light { flex: 0 0 58%; background: var(--paper-edge); }
  .edge-band__dark { flex: 1; background: var(--navy); height: 34px; margin-top: -18px; }
</style>
</head>
<body>
  <section class="card card--front" aria-label="Card front">
    <div class="wordmark"><span class="wordmark__dot"></span><span>Pelton Mortgage</span></div>
  </section>

  <section class="card card--back" aria-label="Card back">
    <div class="wordmark"><span class="wordmark__dot"></span><span>Pelton Mortgage</span></div>

    <div class="person">
      <p class="person__name">Daniel Hartley</p>
      <p class="person__title">President</p>
    </div>
    <div class="divider"></div>
    <address class="address" style="font-style:normal">
      4120 Larkspur Avenue<br>Cedar Grove, NY 11520
    </address>

    <ul class="contact">
      <li>(555) 0142-7730
        <svg viewBox="0 0 10 10"><path d="M2 0.5 L3.6 2.6 L2.8 3.6 Q4 6 6.4 7.2 L7.4 6.4 L9.5 8 L8.4 9.5 Q1 8 0.5 1.6 Z"/></svg></li>
      <li>name@Pelton.com
        <svg viewBox="0 0 10 10"><path d="M0 2 H10 V8.5 H0 Z M0.6 2.4 L5 5.6 L9.4 2.4" stroke="#d6b043" stroke-width=".6"/></svg></li>
      <li>www.Pelton.com
        <svg viewBox="0 0 10 10"><circle cx="5" cy="5" r="4.8"/></svg></li>
    </ul>

    <div class="edge-band">
      <div class="edge-band__light"></div>
      <div class="edge-band__dark"></div>
    </div>
  </section>
</body>
</html>
```